Values Statement poster template

We want to develop a poster template for our company policies and statements which promote our company values in our workplaces.
These documents are important in showing our clients, suppliers and employees who we are and what we stand for.
The graphic design will incorporate our company logo, and be bright, uplifting and inspiring, developing a graphic theme that we can utilise for other company documents. The design will graphically illustrate and support our values statement, with colour and modern design.
This values poster will be the first in a series of documents using the same theme.The format will be a4 and a3 portrait
We are an environmental service business specialising in rehabilitation and revegetation

Target Market(s)

Tier one clients in industry, Mining, Construction and agriculture

Font styles to use
Other font styles liked:
• calibri

Requirements
Must have
• Professional , high end feel, able to read clearly on a poster
Nice to have
• graphic design elements, symbols, etc which support the message, that can be carried through to various documents such as quality, environmental, safety policies
A bright theme which ties in with our logo colours.

```html
<!DOCTYPE html>
<html lang="en">
<head>
<meta charset="utf-8">
<title>Verdaleaf – Our Values Poster</title>
<link rel="stylesheet" href="https://fonts.googleapis.com/css2?family=Arimo:ital,wght@0,400;0,700;1,700&family=Arvo:ital@1&family=Kreon:wght@400;500&display=swap">
<style>
:root{
  --backdrop:#e9ece9;
  --paper:#ffffff;
  --forest:#0b6a12;
  --leaf:#2e9a36;
  --cyan:#1aa6c8;
  --orange:#f07a1f;
  --ink:#1e1e1e;
  --white:#ffffff;
}
*{margin:0;padding:0;box-sizing:border-box}
html,body{width:1200px;height:1200px;overflow:hidden;background:var(--backdrop)}
.poster{position:absolute;left:180px;top:11px;width:840px;height:1178px;background:var(--paper);overflow:hidden;font-family:"Arimo",Arial,sans-serif;color:var(--ink)}
.poster-shapes{position:absolute;inset:0}
.abs{position:absolute}
.brand{left:33px;top:46px;display:flex;align-items:center;gap:10px}
.brand-dot{width:30px;height:30px;border-radius:50%;background:var(--orange)}
.brand-name{font-family:"Arimo",Arial,sans-serif;font-weight:700;font-size:36px;color:var(--forest)}
.accent-bar{position:absolute;width:4px;background:var(--forest)}
.accent-bar.on-green{background:var(--orange)}
.title-values{left:33px;top:120px;font-family:"Arvo",Georgia,serif;font-style:italic;font-size:41px;color:var(--orange)}
.lead{left:33px;top:177px;font-size:17px;line-height:1.27}
.kicker{font-weight:700;font-style:italic;font-size:26px;color:var(--cyan);letter-spacing:.2px}
.slab-sub{font-family:"Kreon",Georgia,serif;font-size:24px;color:var(--cyan)}
.slab-head{font-family:"Kreon",Georgia,serif;font-weight:500;font-size:34px;color:var(--cyan);letter-spacing:.6px;white-space:nowrap}
.intro{left:34px;top:313px;font-size:20px}
.point{position:absolute;left:52px;font-size:14.6px;line-height:1.3;padding-left:0}
.point::before{content:"";position:absolute;left:-20px;top:4px;width:9px;height:9px;border-radius:50%;background:var(--orange);box-shadow:5px -3px 0 -1px var(--leaf)}
.right .point{left:526px;color:var(--white);font-size:14.8px}
.right .point::before{background:var(--orange);box-shadow:5px -3px 0 -1px #8fd14f}
.body-copy{font-size:14.8px;line-height:1.3}
.green-head{font-family:"Kreon",Georgia,serif;font-weight:500;font-size:33px;line-height:1.02;color:var(--white);letter-spacing:.6px}
.green-copy{color:var(--white);font-size:15px;line-height:1.27}
.footer{left:0;top:1137px;width:466px;height:41px;background:var(--orange);color:var(--white);font-weight:700;font-size:18px;display:flex;align-items:center;justify-content:center;letter-spacing:.3px}
</style>
</head>
<body>
<main class="poster">
  <svg class="poster-shapes" width="840" height="1178" viewBox="0 0 840 1178">
    <defs>
      <linearGradient id="sky" x1="0" y1="0" x2="0" y2="1">
        <stop offset="0" stop-color="#4f8fd8"/><stop offset="1" stop-color="#9cc4ee"/>
      </linearGradient>
      <linearGradient id="desk" x1="0" y1="0" x2="1" y2="1">
        <stop offset="0" stop-color="#2f7a1e"/><stop offset=".6" stop-color="#8aa850"/><stop offset="1" stop-color="#c9c79a"/>
      </linearGradient>
    </defs>
    <rect class="green-panel" x="473" y="405" width="367" height="773" fill="var(--forest)"/>
    <rect x="621" y="0" width="219" height="165" fill="var(--forest)"/>
    <circle cx="621" cy="165" r="278" fill="var(--forest)"/>
    <circle cx="628" cy="168" r="232" fill="var(--paper)"/>
    <circle cx="628" cy="168" r="199" fill="url(#sky)" role="img" aria-label="Photo of a wooden signpost with arrows reading Values, Mission and Vision against a blue sky"/>
    <path d="M473 1060 Q640 1030 840 1040 L840 1178 L473 1178 Z" fill="url(#desk)" role="img" aria-label="Photo of colleagues working together at a desk with a laptop and papers"/>
  </svg>

  <div class="abs brand"><span class="brand-dot"></span><span class="brand-name">Verdaleaf</span></div>

  <section class="left">
    <span class="accent-bar" style="left:18px;top:131px;height:91px"></span>
    <h1 class="abs title-values">Our Values</h1>
    <p class="abs lead">These are the things we value most,<br>they define the way we do business.</p>

    <span class="accent-bar" style="left:18px;top:251px;height:51px"></span>
    <h2 class="abs kicker" style="left:33px;top:250px">WE VALUE OUR PEOPLE</h2>
    <p class="abs slab-sub" style="left:31px;top:276px">above everything else.</p>
    <p class="abs intro">We demonstrate this by:</p>
    <p class="point" style="top:354px">Providing safe, positive, enjoyable workplaces<br>where everyone feels valued and respected</p>
    <p class="point" style="top:404px">Providing Careers, not Jobs, we grow together</p>
    <p class="point" style="top:436px">Encouraging inclusion, participation and collaboration</p>
    <p class="point" style="top:469px">Recognising and rewarding contribution and excellence</p>
    <p class="point" style="top:501px">Supporting our people through tough times</p>

    <span class="accent-bar" style="left:18px;top:540px;height:52px"></span>
    <h2 class="abs slab-head" style="left:29px;top:534px">WE DO GOOD THINGS</h2>
    <p class="abs slab-sub" style="left:35px;top:568px">for the planet.</p>
    <p class="point" style="top:612px;left:54px">Our products are helping revegetate Australia, which<br>we are tremendously proud of.</p>
    <p class="point" style="top:655px;left:54px">We minimise our environmental impact in everything<br>we do.</p>

    <span class="accent-bar" style="left:18px;top:702px;height:39px"></span>
    <h2 class="abs slab-head" style="left:27px;top:702px">WE SET THE STANDARD</h2>
    <p class="point" style="top:749px;left:56px">We are uncompromising on quality</p>
    <p class="point" style="top:775px;left:56px">We are the best at what we do, and we do what<br>we are best at</p>
    <p class="point" style="top:815px;left:56px">We are always improving</p>
    <p class="point" style="top:839px;left:56px">We are pioneering</p>

    <span class="accent-bar" style="left:18px;top:873px;height:43px"></span>
    <h2 class="abs slab-head" style="left:27px;top:873px">WE SUCCEED TOGETHER</h2>
    <p class="abs body-copy" style="left:30px;top:917px">We believe in win-win relationships. When our business<br>is profitable everyone benefits, our owners employees,<br>clients and the community. At Verdaleaf we:</p>
    <p class="point" style="top:992px;left:56px">Work as a team, we get it done together</p>
    <p class="point" style="top:1017px;left:56px">We treat our suppliers and subcontractors<br>like they are part of the team.</p>
    <p class="point" style="top:1065px;left:56px">Are building on our success, and growing together</p>
    <p class="point" style="top:1090px;left:56px">Choose to work with employees, customers and<br>suppliers who fit our values</p>
  </section>

  <section class="right">
    <span class="accent-bar on-green" style="left:490px;top:444px;height:53px"></span>
    <h2 class="abs green-head" style="left:501px;top:440px">OUR WORKPLACES<br>ARE SAFE</h2>
    <p class="abs green-copy" style="left:495px;top:517px;width:330px">There is nothing more important to us than our people going home healthy and safe every day. We won’t accept anything less. We believe safety is a management choice. By providing safe work systems, and education we achieve our daily goal of Zero Harm. At Verdaleaf we ;</p>
    <p class="point" style="top:672px">Take the time to make our work areas<br>safe, whatever it takes</p>
    <p class="point" style="top:723px">Don’t accept shortcuts</p>
    <p class="point" style="top:756px">Look out for each other</p>
    <p class="point" style="top:789px">Investigate our incidents and learn from<br>them, we won’t accept repeats</p>
    <p class="point" style="top:841px">Are constantly looking for ways to<br>improve the safety of our workplaces.</p>
    <p class="point" style="top:891px">Think safe, work safer, go home safe!</p>

    <span class="accent-bar on-green" style="left:491px;top:938px;height:39px"></span>
    <h2 class="abs green-head" style="left:508px;top:940px">WE GIVE BACK</h2>
    <p class="abs green-copy" style="left:509px;top:985px;width:300px">We appreciate our success and we give back by supporting our community, and those less fortunate.</p>
  </section>

  <footer class="abs footer">www.verdaleaf-example.com</footer>
</main>
</body>
</html>
```